Simple and Clean business card design

We would like the design to be simple clean and to incorporate our colors.

We are open to your design and talent, we have the dots in our logo as we think of it as data points and we connect data points for people.

We are open to see the great creative and clean design you bring to the table

Contact Information for Business Card

please include: name, position, email, phone and website

Font styles to use
Sans Serif

Requirements
Must have
• my colors incorporated, simplicity
Nice to have
• lots of white space, simplicity
Should not have
• complexicity/ complex art

```html
<!DOCTYPE html>
<html lang="en">
<head>
<meta charset="utf-8">
<title>Bloomly business card</title>
<link rel="stylesheet" href="https://fonts.googleapis.com/css2?family=Poppins:wght@400;600;700&display=swap">
<style>
  :root {
    --page: #e9e7e3;
    --card-white: #ffffff;
    --card-black: #000000;
    --ink: #111111;
    --blue: #4285f4;
    --green: #34a853;
    --yellow: #fbbc05;
    --red: #ea4335;
    --white: #ffffff;
    --soft-blue: #dae6fb;
    --soft-green: #d5ecdc;
    --soft-yellow: #fdf1c8;
    --soft-pink: #fadad8;
  }
  * { margin: 0; padding: 0; box-sizing: border-box; }
  html, body { width: 1200px; height: 900px; overflow: hidden; }
  body {
    background: var(--page);
    font-family: "Poppins", sans-serif;
    display: flex;
    flex-direction: column;
    align-items: center;
    justify-content: center;
    gap: 40px;
  }
  .card {
    width: 700px;
    height: 400px;
    border-radius: 26px;
    position: relative;
    overflow: hidden;
    box-shadow: 0 6px 18px rgba(0,0,0,0.15);
  }
  .card-front { background: var(--card-white); color: var(--ink); }
  .card-back { background: var(--card-black); color: var(--white); }

  .soft-circle { position: absolute; border-radius: 50%; }
  .soft-blue { left: 110px; top: 175px; width: 240px; height: 240px; background: var(--soft-blue); }
  .soft-green { left: 300px; top: 45px; width: 150px; height: 150px; background: var(--soft-green); }
  .soft-yellow { left: 470px; top: 95px; width: 100px; height: 100px; background: var(--soft-yellow); }
  .soft-pink { left: 580px; top: 165px; width: 82px; height: 82px; background: var(--soft-pink); }

  .brand { display: flex; align-items: center; gap: 12px; font-weight: 700; line-height: 1; position: absolute; }
  .brand-dot { border-radius: 50%; background: var(--blue); flex: none; }

  .card-front .brand { left: 48px; top: 48px; font-size: 56px; color: var(--ink); }
  .card-front .brand-dot { width: 26px; height: 26px; }

  .details { position: absolute; left: 330px; top: 170px; }
  .company { font-size: 32px; font-weight: 700; line-height: 1.1; }
  .role { font-size: 24px; color: var(--blue); margin-bottom: 18px; }
  .contact-list { list-style: none; }
  .contact-item { display: flex; align-items: center; gap: 12px; font-size: 20px; line-height: 1.7; }
  .contact-item svg { width: 18px; height: 18px; flex: none; }

  .card-back .brand { left: 80px; top: 105px; font-size: 104px; color: var(--white); gap: 16px; }
  .card-back .brand-dot { width: 40px; height: 40px; }
  .back-site { position: absolute; left: 86px; top: 270px; font-size: 22px; }
  .site-blue { color: var(--blue); }
  .site-red { color: var(--red); }
  .site-green { color: var(--green); }
</style>
</head>
<body>
  <section class="card card-front" aria-label="Card front">
    <span class="soft-circle soft-blue"></span>
    <span class="soft-circle soft-green"></span>
    <span class="soft-circle soft-yellow"></span>
    <span class="soft-circle soft-pink"></span>
    <div class="brand"><span class="brand-dot"></span>Bloomly</div>
    <div class="details">
      <p class="company">Bloomly.Co</p>
      <p class="role">Founder/ CEO</p>
      <ul class="contact-list">
        <li class="contact-item">
          <svg viewBox="0 0 24 24" aria-hidden="true"><path fill="var(--green)" d="M6.6 10.8a15.1 15.1 0 0 0 6.6 6.6l2.2-2.2c.3-.3.7-.4 1-.2 1.1.4 2.3.6 3.6.6.6 0 1 .4 1 1V20c0 .6-.4 1-1 1A17 17 0 0 1 3 4c0-.6.4-1 1-1h3.5c.6 0 1 .4 1 1 0 1.3.2 2.5.6 3.6.1.3 0 .7-.2 1z"/></svg>
          555-214-3087
        </li>
        <li class="contact-item">
          <svg viewBox="0 0 24 24" aria-hidden="true"><rect x="2" y="5" width="20" height="14" rx="2" fill="var(--yellow)"/><path d="M3 6l9 7 9-7" fill="none" stroke="#fff" stroke-width="1.6"/></svg>
          sam.rivers@bloomly.co
        </li>
        <li class="contact-item">
          <svg viewBox="0 0 24 24" aria-hidden="true"><circle cx="12" cy="12" r="10" fill="var(--red)"/><path d="M2 12h20M12 2c3 3 3 17 0 20M12 2c-3 3-3 17 0 20" fill="none" stroke="#fff" stroke-width="1.4"/></svg>
          www.bloomly.co
        </li>
      </ul>
    </div>
  </section>

  <section class="card card-back" aria-label="Card back">
    <div class="brand"><span class="brand-dot"></span>Bloomly</div>
    <p class="back-site"><span class="site-blue">www.</span><span class="site-red">bloomly</span><span class="site-green">.co</span></p>
  </section>
</body>
</html>
```